Infographic for venture capital "investment adviser" model

We need an infographic for users to easily visualize and grasp what is meant by a "investment adviser" model. The attached .pdf has the copy and my (very bad) rough design of the graphic. Needs to be professionally done now.

Description of Venture Capital: a venture capitalist creates a "fund", they then go raise money from investors for that fund. Once they have money, they then invest it in various companies or assets. As money com comes back to the fund from the investments, the venture capitalist pays the funds investors (and themselves).

A venture capitalist will usually manage multiple "funds". That's why there is a management company (the VC) that is hired by each fund they create. The VC management company is paid an annual fee of 2%, and then they also get 20% of the profits - that's what the "2%/20%" represents in the graphic.

Target Market(s)

Venture capitalists, investment advisers, wall street brokers

Industry/Entity Type

Venture Capital

Font styles to use
Serif

Colors
f37122
f68d4c
3276b5

Requirements
Must have
• Our logo (attached)
• Display 3 different funds, all being managed by a single entity
• Fyi - I just uploaded a new graphic of what the "website" should look like (can be similar, doesn't have to be this image...just something to show a crowdfunding website)
Nice to have
• Neat representations of investors and of a funds portfolio companies

```html
<!DOCTYPE html>
<html lang="en">
<head>
<meta charset="utf-8">
<title>Funding Platform – VC Investment Adviser Model</title>
<link href="https://fonts.googleapis.com/css2?family=Open+Sans:wght@400;600;700;800&family=Roboto+Condensed:wght@400;700&display=swap" rel="stylesheet">
<style>
  :root {
    --orange: #f37122;
    --orange-light: #f68d4c;
    --blue: #3276b5;
    --blue-dark: #1f5f9c;
    --ink: #1a1a1a;
    --paper: #ffffff;
    --stage: #e9e6e1;
    --glow: #dcebf8;
    --note: #e0261b;
  }
  * { margin: 0; padding: 0; box-sizing: border-box; }
  html, body { width: 1200px; height: 1000px; overflow: hidden; background: var(--stage); }
  .canvas { position: relative; width: 1200px; height: 1000px; }
  .sheet {
    position: absolute; left: 62px; top: 18px; width: 1080px; height: 957px;
    background: radial-gradient(ellipse 420px 360px at 536px 510px, var(--glow) 0%, var(--paper) 100%);
    box-shadow: 0 2px 10px rgba(0,0,0,.25);
  }
  .sheet-title {
    height: 54px; background: linear-gradient(#3a84c6, var(--blue-dark));
    color: #fff; font: 700 23px/54px "Open Sans", sans-serif; text-align: center; letter-spacing: .3px;
  }
  .sheet-subtitle {
    height: 33px; border-bottom: 1px solid #9fbbd6;
    color: var(--orange); font: 400 18px/33px "Open Sans", sans-serif; text-align: center;
  }
  .diagram { position: absolute; left: 0; top: 0; }
  .label { font-family: "Roboto Condensed", sans-serif; }
  .head { font-family: "Open Sans", sans-serif; }
</style>
</head>
<body>
<div class="canvas">
  <section class="sheet">
    <h1 class="sheet-title">FUNDING PLATFORM</h1>
    <p class="sheet-subtitle">VC “Investment Adviser” Model</p>
  </section>

  <svg class="diagram" width="1200" height="1000" viewBox="0 0 1200 1000" xmlns="http://www.w3.org/2000/svg">
    <defs>
      <marker id="arrow-blue" viewBox="0 0 10 10" refX="9" refY="5" markerWidth="7" markerHeight="7" orient="auto"><path d="M0 0 L10 5 L0 10 z" fill="#3276b5"/></marker>
      <marker id="arrow-black" viewBox="0 0 10 10" refX="9" refY="5" markerWidth="6" markerHeight="6" orient="auto-start-reverse"><path d="M0 0 L10 5 L0 10 z" fill="#1a1a1a"/></marker>
      <marker id="arrow-orange" viewBox="0 0 10 10" refX="9" refY="5" markerWidth="7" markerHeight="7" orient="auto"><path d="M0 0 L10 5 L0 10 z" fill="#f37122"/></marker>
      <filter id="soft" x="-20%" y="-20%" width="140%" height="140%"><feDropShadow dx="0" dy="2" stdDeviation="3" flood-opacity=".25"/></filter>
      <symbol id="investor-icon" viewBox="0 0 40 34">
        <circle cx="13" cy="7" r="6" fill="#3276b5"/>
        <path d="M2 22 Q2 14 13 14 Q24 14 24 22 Z" fill="#3276b5"/>
        <g fill="#3276b5" stroke="#fff" stroke-width="1">
          <ellipse cx="10" cy="30" rx="7" ry="3"/><ellipse cx="10" cy="27" rx="7" ry="3"/><ellipse cx="10" cy="24" rx="7" ry="3"/>
          <ellipse cx="28" cy="30" rx="7" ry="3"/><ellipse cx="28" cy="27" rx="7" ry="3"/><ellipse cx="28" cy="24" rx="7" ry="3"/>
          <ellipse cx="19" cy="31" rx="7" ry="3"/>
        </g>
      </symbol>
      <symbol id="fee-pie" viewBox="-30 -30 60 60">
        <circle r="28" fill="#3276b5" stroke="#fff" stroke-width="1"/>
        <path d="M0 0 L0 -28 A28 28 0 0 1 9 -26.5 Z" fill="#f37122"/>
        <line x1="0" y1="0" x2="0" y2="-28" stroke="#fff" stroke-width="1"/>
        <text y="6" text-anchor="middle" fill="#fff" font-family="Roboto Condensed, sans-serif" font-size="15">2%/20%</text>
      </symbol>
    </defs>

    <!-- flow lines: website -->
    <g fill="none" stroke="#3276b5" stroke-width="2">
      <path d="M323 688 V182 H356" marker-end="url(#arrow-blue)"/>
      <path d="M876 688 V182 H846" marker-end="url(#arrow-blue)"/>
      <path d="M598 250 V224" marker-end="url(#arrow-blue)"/>
    </g>

    <!-- flow lines: broker-dealer and funds -->
    <g fill="none" stroke="#1a1a1a" stroke-width="1.5">
      <path d="M357 305 H103 V907 H381" marker-end="url(#arrow-black)"/>
      <path d="M192 771 V880 H381" marker-end="url(#arrow-black)"/>
      <path d="M1015 771 V880 H824" marker-end="url(#arrow-black)"/>
      <path d="M500 305 H546" marker-start="url(#arrow-black)" marker-end="url(#arrow-black)"/>
      <path d="M652 305 H693" marker-end="url(#arrow-black)"/>
      <path d="M269 735 H314" marker-start="url(#arrow-black)" marker-end="url(#arrow-black)"/>
      <path d="M420 735 H462" marker-end="url(#arrow-black)"/>
      <path d="M884 735 H938" marker-start="url(#arrow-black)" marker-end="url(#arrow-black)"/>
      <path d="M780 735 H739" marker-end="url(#arrow-black)"/>
    </g>

    <!-- fee arrows -->
    <g fill="none" stroke="#f37122" stroke-width="2">
      <path d="M598 356 V412" marker-end="url(#arrow-orange)"/>
      <path d="M390 684 L486 604" marker-end="url(#arrow-orange)"/>
      <path d="M808 684 L712 604" marker-end="url(#arrow-orange)"/>
    </g>

    <!-- website -->
    <g class="website">
      <rect x="368" y="139" width="465" height="79" fill="#f68d4c" stroke="#f37122" stroke-width="3"/>
      <text x="404" y="186" fill="#fff" class="head" font-size="16"><tspan font-weight="800">WEBSITE</tspan> (aka “Funding Platform”)</text>
      <g class="functions-stack">
        <path d="M681 194 V216 A64 10 0 0 0 809 216 V194 Z" fill="#fff" stroke="#3276b5" stroke-width="1.5"/>
        <path d="M681 170 V194 A64 10 0 0 0 809 194 V170 Z" fill="#fff" stroke="#3276b5" stroke-width="1.5"/>
        <path d="M681 150 V170 A64 10 0 0 0 809 170 V150 Z" fill="#3276b5"/>
        <ellipse cx="745" cy="150" rx="64" ry="10" fill="#5b95cb"/>
        <text x="745" y="168" text-anchor="middle" fill="#fff" class="label" font-size="15">FUNCTIONS</text>
        <text x="745" y="189" text-anchor="middle" fill="#3276b5" class="label" font-size="11">*Advertising /Mktg</text>
        <text x="745" y="216" text-anchor="middle" fill="#3276b5" class="label" font-size="11">*SaaS</text>
      </g>
    </g>

    <!-- investors boxes -->
    <g class="investors">
      <rect x="357" y="272" width="140" height="68" fill="#fff" stroke="#3276b5" stroke-width="1.5"/>
      <use href="#investor-icon" x="366" y="290" width="38" height="32"/>
      <text x="410" y="311" fill="#3276b5" class="label" font-size="17">INVESTORS</text>

      <rect x="126" y="700" width="140" height="70" fill="#fff" stroke="#3276b5" stroke-width="1.5"/>
      <use href="#investor-icon" x="135" y="719" width="38" height="32"/>
      <text x="179" y="741" fill="#3276b5" class="label" font-size="17">INVESTORS</text>

      <rect x="941" y="700" width="139" height="70" fill="#fff" stroke="#3276b5" stroke-width="1.5"/>
      <use href="#investor-icon" x="950" y="719" width="38" height="32"/>
      <text x="994" y="741" fill="#3276b5" class="label" font-size="17">INVESTORS</text>
    </g>

    <!-- portfolio boxes -->
    <g class="portfolio" fill="#fff" text-anchor="middle" font-family="Roboto Condensed, sans-serif">
      <rect x="697" y="272" width="96" height="68" fill="#3276b5"/>
      <text x="745" y="297" font-size="16">PORTFOLIO</text>
      <text x="745" y="316" font-size="13">Company</text>
      <text x="745" y="331" font-size="13">or Asset</text>

      <rect x="466" y="700" width="96" height="70" fill="#3276b5"/>
      <text x="514" y="726" font-size="16">PORTFOLIO</text>
      <text x="514" y="746" font-size="13">Company</text>
      <text x="514" y="761" font-size="13">or Asset</text>

      <rect x="639" y="700" width="96" height="70" fill="#3276b5"/>
      <text x="687" y="726" font-size="16">PORTFOLIO</text>
      <text x="687" y="746" font-size="13">Company</text>
      <text x="687" y="761" font-size="13">or Asset</text>
    </g>

    <!-- funds -->
    <g class="funds" text-anchor="middle" fill="#fff" font-family="Roboto Condensed, sans-serif">
      <circle cx="598" cy="305" r="53" fill="#fff" filter="url(#soft)"/>
      <circle cx="598" cy="305" r="46" fill="#f37122"/>
      <text x="598" y="305" font-size="25">FUND</text>
      <text x="598" y="327" font-size="16">SPV 1</text>

      <circle cx="367" cy="735" r="53" fill="#fff" filter="url(#soft)"/>
      <circle cx="367" cy="735" r="46" fill="#f37122"/>
      <text x="367" y="735" font-size="25">FUND</text>
      <text x="367" y="757" font-size="16">SPV 2</text>

      <circle cx="831" cy="735" r="53" fill="#fff" filter="url(#soft)"/>
      <circle cx="831" cy="735" r="46" fill="#f37122"/>
      <text x="831" y="735" font-size="25">FUND</text>
      <text x="831" y="757" font-size="16">SPV 3</text>
    </g>

    <!-- fee pies -->
    <use href="#fee-pie" x="527" y="352" width="56" height="56"/>
    <use href="#fee-pie" x="392" y="589" width="56" height="56"/>
    <use href="#fee-pie" x="757" y="589" width="56" height="56"/>

    <!-- management company -->
    <g class="ventures">
      <circle cx="598" cy="536" r="131" fill="#fff" filter="url(#soft)"/>
      <clipPath id="ventures-clip"><circle cx="598" cy="536" r="120"/></clipPath>
      <g clip-path="url(#ventures-clip)">
        <rect x="478" y="416" width="240" height="240" fill="#f37122"/>
        <rect x="478" y="416" width="240" height="70" fill="#e9661a"/>
        <line x1="478" y1="486" x2="718" y2="486" stroke="#f68d4c" stroke-width="1"/>
      </g>
      <text x="598" y="476" text-anchor="middle" fill="#fff" class="head" font-weight="700" font-size="17">VENTURES</text>
      <g class="team-icon">
        <circle cx="580" cy="511" r="9" fill="#fff"/><path d="M565 548 Q565 525 580 525 Q595 525 595 548 Z" fill="#fff"/>
        <circle cx="616" cy="511" r="9" fill="#fff"/><path d="M601 548 Q601 525 616 525 Q631 525 631 548 Z" fill="#fff"/>
        <circle cx="598" cy="507" r="11" fill="#3276b5"/><path d="M579 552 Q579 522 598 522 Q617 522 617 552 Z" fill="#3276b5"/>
      </g>
      <text x="598" y="572" text-anchor="middle" fill="#fff" class="head" font-weight="700" font-size="15">IA Management Group</text>
      <text x="598" y="605" text-anchor="middle" fill="#fff" class="head" font-size="12">Fee on assets of the funds,</text>
      <text x="598" y="621" text-anchor="middle" fill="#fff" class="head" font-size="12">Plus carried interest</text>
    </g>

    <!-- broker-dealer -->
    <g class="broker">
      <rect x="384" y="838" width="438" height="77" fill="#fff" stroke="#f37122" stroke-width="3"/>
      <text x="404" y="884" fill="#3276b5" class="head" font-weight="800" font-size="14">BROKER - DEALER - CAPITAL BRIDGE</text>
      <g class="functions-stack" text-anchor="middle" font-family="Roboto Condensed, sans-serif">
        <path d="M691 908 V922 A61 9 0 0 0 813 922 V908" fill="#3276b5"/>
        <path d="M691 888 V903 A61 9 0 0 0 813 903 V888" fill="#3276b5"/>
        <path d="M691 868 V883 A61 9 0 0 0 813 883 V868" fill="#3276b5"/>
        <path d="M691 846 V863 A61 9 0 0 0 813 863 V846" fill="#3276b5"/>
        <path d="M691 820 V841 A61 9 0 0 0 813 841 V820" fill="#f37122"/>
        <ellipse cx="752" cy="820" rx="61" ry="9" fill="#3276b5"/>
        <g fill="none" stroke="#fff" stroke-width="1.2">
          <path d="M691 841 A61 9 0 0 0 813 841"/><path d="M691 863 A61 9 0 0 0 813 863"/>
          <path d="M691 883 A61 9 0 0 0 813 883"/><path d="M691 903 A61 9 0 0 0 813 903"/>
        </g>
        <text x="752" y="840" fill="#fff" font-size="15">FUNCTIONS</text>
        <text x="752" y="862" fill="#fff" font-size="11">*Escrow</text>
        <text x="752" y="882" fill="#fff" font-size="11">*State blue sky</text>
        <text x="752" y="902" fill="#fff" font-size="11">*AML</text>
        <text x="752" y="921" fill="#fff" font-size="10.5">*Payment processing Etc</text>
      </g>
    </g>

    <!-- footer -->
    <text x="88" y="957" fill="#e0261b" font-family="Open Sans, sans-serif" font-size="10">*Note: <tspan font-weight="700" text-decoration="underline">NOT</tspan> intended as legal advice, consult your securities attorney</text>
    <text x="1118" y="953" text-anchor="end" fill="#333" font-family="Open Sans, sans-serif" font-size="11">© CapitalBridge Technologies, LLC 2015 All Rights Reserved</text>
  </svg>
</div>
</body>
</html>
```